Sales Brochure- Generic Line Card 215mm x 140mm

Design a double-sided brochure similar to the attached sample. Cover Page contains a logo and theme that never changes. However, the background picture and the description text on the lower corner will be changed to advertise multiple services. Reverse-side contains Detailed Descriptive text related to the picture on Cover Page as well as Logo and Contact information for the business. Use the Ridgeline Controls website www.ridgelinecontrols.ca for theme, color and contact information. Also, use attached business card design for theme to match. Use the supplied logo. SIZE 215mm x 140mm

Font styles to use
Sans Serif

Colors

Designer to choose colors to be used in the design.

Requirements
Must have
• Look Similar to Sample Brochure but include Ridgeline Controls theme and colors

```html
<!DOCTYPE html>
<html lang="en">
<head>
<meta charset="utf-8">
<title>Ridgeline Controls – Line Card</title>
<link href="https://fonts.googleapis.com/css2?family=Michroma&family=Montserrat:ital,wght@0,400;0,600;1,400&family=Orbitron:wght@800&display=swap" rel="stylesheet">
<style>
  :root{
    --stage:#3a2a20;
    --teal:#0f6f73;
    --teal-bright:#1f8d93;
    --teal-deep:#0d3c3e;
    --ink:#1b1f20;
    --panel:#242b2d;
    --paper:#f2f2f2;
    --text-light:#e6ecec;
  }
  *{margin:0;padding:0;box-sizing:border-box}
  html,body{width:1200px;height:903px;overflow:hidden;background:var(--stage)}
  .canvas{position:relative;width:1200px;height:903px}

  .card{position:absolute;width:578px;height:376px;overflow:hidden;box-shadow:0 8px 24px rgba(0,0,0,.45)}

  /* Cover */
  .cover{left:177px;top:54px;background:var(--teal-deep)}
  .cover__strip{position:absolute;left:0;top:0;width:61px;height:100%;background:#0c2e30}
  .cover__rule{position:absolute;left:61px;top:0;width:2px;height:100%;background:#fff}
  .cover__photo{position:absolute;left:63px;top:0;right:0;bottom:0;
    background:radial-gradient(ellipse at 45% 35%,#2a9a98 0%,#187a7a 40%,#0d4f51 75%,#0a3537 100%)}
  .brand-pill{position:absolute;display:flex;align-items:center;gap:8px;background:var(--paper);border-radius:0 31px 31px 0}
  .cover .brand-pill{left:63px;top:16px;width:238px;height:62px;padding-left:16px}
  .brand-pill__mark{width:16px;height:16px;background:var(--teal);flex:none}
  .brand-pill__name{font-family:"Montserrat",sans-serif;font-weight:600;font-size:15px;letter-spacing:.5px;color:var(--ink);white-space:nowrap}
  .tagline-pill{position:absolute;right:0;top:294px;width:241px;height:76px;background:var(--paper);
    border-radius:38px 0 0 38px;border:2px solid #fff;display:flex;flex-direction:column;justify-content:center;align-items:flex-end;padding-right:30px;
    font-family:"Michroma",sans-serif;font-size:17px;line-height:22px;font-weight:400;letter-spacing:.5px}
  .tagline-pill .accent{color:var(--teal-bright)}
  .tagline-pill .dark{color:var(--ink)}

  /* Reverse */
  .reverse{left:446px;top:464px;background:linear-gradient(180deg,#283032 0%,var(--panel) 60%,#1f2527 100%)}
  .reverse__heading{position:absolute;left:0;right:0;top:28px;text-align:center;font-family:"Orbitron",sans-serif;font-weight:800;font-size:24px;color:var(--teal-bright);letter-spacing:.3px}
  .reverse__body{position:absolute;left:32px;width:514px;top:72px;font-family:"Montserrat",sans-serif;font-size:10.6px;line-height:12.8px;color:var(--text-light)}
  .reverse__body p{text-align:justify;margin-bottom:13px}
  .reverse__body .welcome{font-weight:600;margin-top:31px;margin-bottom:13px}
  .reverse__body .inquiry strong{font-weight:600}
  .footer-band{position:absolute;left:0;right:0;top:312px;height:64px;background:var(--teal)}
  .reverse .brand-pill{left:0;top:322px;width:204px;height:50px;padding-left:20px;border-radius:0 25px 25px 0}
  .reverse .brand-pill__name{font-size:13px}
  .contact{position:absolute;top:336px;display:flex;align-items:center;gap:10px;font-family:"Montserrat",sans-serif;font-style:italic;font-size:13.5px;color:#fff}
  .contact--phone{left:226px}
  .contact--web{left:366px}
  .contact svg{width:14px;height:14px;stroke:#cfe6e6;fill:none;stroke-width:1.5}
</style>
</head>
<body>
<div class="canvas">

  <section class="card cover">
    <div class="cover__strip"></div>
    <div class="cover__photo" role="img" aria-label="Teal-toned photograph of a CNC lathe turret and spindle"></div>
    <div class="cover__rule"></div>
    <div class="brand-pill"><span class="brand-pill__mark"></span><span class="brand-pill__name">RIDGELINE CONTROLS</span></div>
    <div class="tagline-pill">
      <span class="accent">PIONEERING</span>
      <span class="dark">RESPONSIVE</span>
      <span class="accent">MACHINING</span>
    </div>
  </section>

  <section class="card reverse">
    <h1 class="reverse__heading">EDMONTON CNC MACHINING</h1>
    <div class="reverse__body">
      <p>Canada’s only Responsive Machine Shop. Offering production CNC Machining, Swiss Screw Machining, Automated Manufacturing, Robotic Machine Tending, Threading, Prototyping and 24/7 Service, Repair and Welding.</p>
      <p>Located in Western Canada, Ridgeline Controls is strategically positioned to service energy, oil &amp; gas, mining, architectural and agricultural industries. Our Edmonton based facility is connected to our customers by land, sea and air with export services available to the US and UK.</p>
      <p>We support a large network of diversified clients and pursue new opportunities in all commercial and industrial sectors. Our focus in Responsiveness enables all of our clients to execute their growth initiatives. Contact our Sales Representatives to begin the conversation.</p>
      <p class="welcome">We welcome and appreciate your interest in our company.</p>
      <p class="inquiry"><strong>Inquiries:</strong> info@ridgelinecontrols.ca</p>
    </div>
    <div class="footer-band"></div>
    <div class="brand-pill"><span class="brand-pill__mark"></span><span class="brand-pill__name">RIDGELINE CONTROLS</span></div>
    <div class="contact contact--phone">
      <svg viewBox="0 0 16 16"><path d="M3 2l3 0 1 4-2 1c1 2 2 3 4 4l1-2 4 1 0 3c-6 1-12-5-11-11z"/></svg>
      <span>780 555 0142</span>
    </div>
    <div class="contact contact--web">
      <svg viewBox="0 0 16 16"><circle cx="8" cy="8" r="6.5"/><ellipse cx="8" cy="8" rx="3" ry="6.5"/><path d="M1.5 8h13"/></svg>
      <span>www.ridgelinecontrols.ca</span>
    </div>
  </section>

</div>
</body>
</html>
```